Brightleaf Practice Partners, Inc (www.brightleafpracticepartnrs.example) would like to design a website to convey a level of professionalism to healthcare providers that we are the place form them to visit for Contin. Education, Marketing and Management, Joint Venture Partnerships, etc.
We think we would like a WP Site so that we can use the dynamic and static sides of it's capabilities. We also want to have something that acts as a membership side where members can post their Bio and CV's and prospective employers can post help wanted ads.

Target Market(s)

Pediatricians, Pediatric Dentist, Employers seeking these doctors

Industry/Entity Type

Healthcare

Requirements
Must have
• Services:
Resumes/Bio
Help Wanted
Continuing Education Programs
Marketing & Management

```html
<!DOCTYPE html>
<html lang="en">
<head>
<meta charset="utf-8">
<title>BPP – Post your Resume Now</title>
<link href="https://fonts.googleapis.com/css2?family=Ubuntu:ital,wght@0,300;0,400;0,500;1,300;1,400&display=swap" rel="stylesheet">
<style>
:root{
  --navy:#1f2b4b;
  --navy-mid:#263a66;
  --sky:#5fb8ee;
  --sky-light:#9bd5f7;
  --band:#3b9fe0;
  --band-dark:#2a86c6;
  --yellow:#f8d51f;
  --orange:#f39a0c;
  --orange-text:#e8760d;
  --link:#2b8ad4;
  --title:#2f82c9;
  --text:#5a5a5a;
  --dark:#2a2a2a;
  --line:#dcdcdc;
  --footer:#f1f1f1;
}
*{box-sizing:border-box;margin:0;padding:0}
html,body{width:888px;height:1200px;overflow:hidden;background:#fff}
body{font-family:"Ubuntu",sans-serif;color:var(--text);position:relative}
a{color:inherit;text-decoration:none}
.abs{position:absolute}

.topbar{left:0;top:0;width:888px;height:29px;background:var(--navy)}
.toplinks{right:50px;top:8px;font-size:10px;color:#c9d2e6}
.toplinks span{margin:0 5px}

.header{left:0;top:29px;width:888px;height:91px;background:linear-gradient(#24365e,#2a3f6c)}
.brand{left:39px;top:29px;font-size:30px;font-weight:500;color:#fff;letter-spacing:1px}
.nav{left:364px;top:47px;display:flex;align-items:center;font-size:13px;color:#fff}
.nav a{padding:5px 0}
.nav .sep{margin:0 19px;color:#dfe6f2}
.nav .active{background:#17223d;border-radius:14px;padding:6px 20px;margin-right:19px}

.hero{left:0;top:120px;width:888px;height:260px;overflow:hidden;
  background:radial-gradient(circle at 650px 110px,#bfe6fb 0,#7cc6f2 35%,#4ba8e6 75%,#3b9adc 100%)}
.hero-photo{left:529px;top:0;width:277px;height:260px;
  background:linear-gradient(180deg,rgba(120,80,50,.55) 0,rgba(235,200,175,.75) 45%,rgba(255,255,255,.85) 100%);
  border-radius:120px 120px 0 0}
.hero-box{left:29px;top:30px;width:424px;height:188px;border-radius:10px;background:rgba(120,190,240,.55);box-shadow:0 2px 6px rgba(0,60,120,.12)}
.hero-title{left:25px;top:20px;font-size:33px;font-weight:300;color:#fff}
.hero-copy{left:25px;top:65px;width:385px;font-size:10.5px;line-height:16px;color:#fff}
.resume-input{left:24px;top:128px;width:242px;height:29px;background:#fff;border-radius:4px 0 0 4px;font-size:12px;color:#888;padding:7px 12px}
.browse-btn{left:263px;top:125px;width:101px;height:34px;background:var(--yellow);border-radius:7px;font-size:14px;color:#333;text-align:center;line-height:34px}

.features{left:0;top:380px;width:888px;height:54px;background:var(--band);border-bottom:3px solid var(--band-dark);display:flex}
.feature{height:51px;display:flex;align-items:center;color:#fff;font-size:17px;font-weight:300;border-right:1px solid rgba(255,255,255,.35)}
.feature svg{margin-right:10px}
.feature:last-child{border-right:none}

.card{top:457px;width:275px;height:136px;border:1px solid var(--line);border-radius:3px;background:#fff;box-shadow:0 1px 2px rgba(0,0,0,.06)}
.card h3{position:absolute;left:18px;top:13px;font-size:17px;font-weight:300;color:var(--title)}
.card p{position:absolute;left:18px;top:44px;width:245px;font-size:9.6px;line-height:14.7px;color:var(--text)}
.readmore{position:absolute;left:19px;top:108px;display:flex;align-items:center;font-size:12.5px;color:var(--link)}
.readmore svg{margin-right:5px}

.panel{top:603px;height:515px;border:1px solid var(--line);border-radius:3px}
.panel h2{position:absolute;left:24px;top:12px;font-size:17px;font-weight:400;color:var(--dark)}
.resumes{left:16px;width:557px;background:#fff}
.stories{left:578px;width:299px;background:#fafafa}

.candidate{left:21px;width:520px;height:100px}
.avatar{left:0;top:0;width:86px;height:73px;border:1px solid var(--line);border-radius:3px;
  background:linear-gradient(180deg,#f3f3f3 0,#d9c3a5 45%,#5aa9e6 100%)}
.candidate h4{position:absolute;left:94px;top:0;font-size:12.5px;font-weight:400;color:var(--dark)}
.candidate p{position:absolute;left:94px;top:19px;width:410px;font-size:9.6px;line-height:13px}
.quals{position:absolute;left:95px;top:48px;font-size:9.6px;color:var(--orange-text)}
.quals span{margin:0 6px;color:#999}
.details{position:absolute;left:94px;top:70px;background:var(--orange);color:#fff;font-size:9.6px;padding:3px 10px;border-radius:3px}

.story{left:12px;width:275px;height:150px}
.story-photo{left:0;top:0;width:77px;height:66px;border:2px solid #fff;box-shadow:0 0 0 1px var(--line);background:linear-gradient(160deg,#e6eef3,#b48f74 55%,#7fa4c0)}
.story blockquote{position:absolute;left:86px;top:0;width:180px;font-size:9.3px;line-height:14.8px;font-style:italic;font-weight:300;color:#555;padding-left:12px}
.story blockquote .q{position:absolute;left:0;top:-4px;font-size:16px;color:#aaa;font-style:normal}
.story blockquote .qe{font-size:16px;color:#aaa;font-style:normal;vertical-align:-5px;margin-left:4px}
.story cite{position:absolute;left:98px;top:117px;font-style:normal;font-size:11.5px;color:var(--dark)}
.divider{left:12px;width:275px;height:1px;background:var(--line)}

.footer{left:0;top:1118px;width:888px;height:82px;background:var(--footer)}
.foot-nav{left:19px;top:14px;font-size:10px;color:#666}
.foot-nav span{margin:0 9px;color:#999}
.copy{left:19px;top:40px;font-size:10px;color:#666}
</style>
</head>
<body>

<div class="abs topbar">
  <div class="abs toplinks">Member Login<span>|</span>Faq's<span>|</span>Sign Up<span>|</span>Support</div>
</div>

<header class="abs header">
  <div class="abs brand">BPP</div>
  <nav class="abs nav">
    <a class="active">Main</a><a>About Us</a><span class="sep">|</span><a>Get Job</a><span class="sep">|</span><a>Post Now</a><span class="sep">|</span><a>Update</a><span class="sep">|</span><a>Contact</a>
  </nav>
</header>

<section class="abs hero">
  <div class="abs hero-photo" role="img" aria-label="Photo of a smiling professional woman"></div>
  <div class="abs hero-box">
    <h1 class="abs hero-title">Post your Resume Now</h1>
    <p class="abs hero-copy">We at Lumenwave provide you the best simple websites too with total work done as using all the best designing and all done so that you can achieve the goal of yours through our work done on your website.</p>
    <div class="abs resume-input">Browse your resume</div>
    <div class="abs browse-btn">Browse Now</div>
  </div>
</section>

<section class="abs features">
  <div class="feature" style="width:212px;padding-left:38px">
    <svg width="26" height="26" viewBox="0 0 26 26" fill="#fff"><path d="M10 1h6v10h5l-8 8-8-8h5z"/><path d="M1 18h4v4h16v-4h4v7H1z"/></svg>Post Wanted Ads
  </div>
  <div class="feature" style="width:170px;padding-left:17px">
    <svg width="26" height="26" viewBox="0 0 26 26" fill="none" stroke="#fff" stroke-width="2"><path d="M4 22l2-7L18 3l5 5-12 12z"/><path d="M15 6l5 5"/><path d="M14 24h10"/></svg>Get Job Offers
  </div>
  <div class="feature" style="width:222px;padding-left:29px">
    <svg width="20" height="20" viewBox="0 0 20 20" fill="#fff"><path d="M7 0h6v7h7v6h-7v7H7v-7H0V7h7z"/></svg>Create Resume now
  </div>
  <div class="feature" style="width:284px;padding-left:23px">
    <svg width="26" height="26" viewBox="0 0 26 26" fill="none" stroke="#fff" stroke-width="3"><path d="M4 12a9 9 0 0 1 16-5"/><path d="M22 14a9 9 0 0 1-16 5"/><path d="M21 2v6h-6" stroke-width="2.5"/><path d="M5 24v-6h6" stroke-width="2.5"/></svg>Check Latest Updates
  </div>
</section>

<article class="abs card" style="left:16px">
  <h3>Job Postings</h3>
  <p>Lumenwave eSolutions is specialized in handling advanced web projects and the ongoing projects that require permanent maintenance and support .We like challenges and do complete</p>
  <a class="readmore"><svg width="14" height="14" viewBox="0 0 14 14" fill="#3b9fe0"><path d="M0 4h6V0l8 7-8 7v-4H0z"/></svg>read more</a>
</article>
<article class="abs card" style="left:303px">
  <h3>Check Profile</h3>
  <p>Lumenwave eSolutions is specialized in handling advanced web projects and the ongoing projects that require permanent maintenance and support .We like challenges and do complete</p>
  <a class="readmore"><svg width="14" height="14" viewBox="0 0 14 14" fill="#3b9fe0"><path d="M0 4h6V0l8 7-8 7v-4H0z"/></svg>read more</a>
</article>
<article class="abs card" style="left:590px">
  <h3>Sign Up Form</h3>
  <p>Lumenwave eSolutions is specialized in handling advanced web projects and the ongoing projects that require permanent maintenance and support .We like challenges and do complete</p>
  <a class="readmore"><svg width="14" height="14" viewBox="0 0 14 14" fill="#3b9fe0"><path d="M0 4h6V0l8 7-8 7v-4H0z"/></svg>read more</a>
</article>

<section class="abs panel resumes">
  <h2>Latest Resume Updates</h2>
  <div class="abs candidate" style="top:53px">
    <div class="abs avatar" role="img" aria-label="Candidate avatar illustration"></div>
    <h4>Candidate Name here</h4>
    <p>We like challenges and do complete these challenge with expertise we like solving questions that arises in such projects as these helps us to grow also.</p>
    <div class="quals">MBBS, PHD In 2005<span>|</span>5 Year Experience</div>
    <a class="details">full details</a>
  </div>
  <div class="abs candidate" style="top:167px">
    <div class="abs avatar" role="img" aria-label="Candidate avatar illustration"></div>
    <h4>Candidate Name here</h4>
    <p>We like challenges and do complete these challenge with expertise we like solving questions that arises in such projects as these helps us to grow also.</p>
    <div class="quals">MBBS, PHD in 2005<span>|</span>5 Year Experience</div>
    <a class="details">full details</a>
  </div>
  <div class="abs candidate" style="top:279px">
    <div class="abs avatar" role="img" aria-label="Candidate avatar illustration"></div>
    <h4>Candidate Name here</h4>
    <p>We like challenges and do complete these challenge with expertise we like solving questions that arises in such projects as these helps us to grow also.</p>
    <div class="quals">MBBS, PHD in 2005<span>|</span>5 Year Experience</div>
    <a class="details">full details</a>
  </div>
  <div class="abs candidate" style="top:396px">
    <div class="abs avatar" role="img" aria-label="Candidate avatar illustration"></div>
    <h4>Candidate Name here</h4>
    <p>We like challenges and do complete these challenge with expertise we like solving questions that arises in such projects as these helps us to grow also.</p>
    <div class="quals">MBBS, PHD in 2005<span>|</span>5 Year Experience</div>
    <a class="details">full details</a>
  </div>
</section>

<section class="abs panel stories">
  <h2 style="left:19px">Sucess Stories</h2>
  <div class="abs story" style="top:49px">
    <div class="abs story-photo" role="img" aria-label="Portrait photo of a male doctor"></div>
    <blockquote><span class="q">&ldquo;</span>BPP &nbsp;is the perfect solution job seekers are looking for, provided you have content with special language (for objective, goals section etc.) ready beforehand. If you don't, you might want to sit down first and think through exactly what you want from a resume.<span class="qe">&rdquo;</span></blockquote>
    <cite>by Author Name</cite>
  </div>
  <div class="abs divider" style="top:188px"></div>
  <div class="abs story" style="top:208px">
    <div class="abs story-photo" role="img" aria-label="Portrait photo of a female professional"></div>
    <blockquote><span class="q">&ldquo;</span>BPP &nbsp;is the perfect solution job seekers are looking for, provided you have content with special language (for objective, goals section etc.) ready beforehand. If you don't, you might want to sit down first and think through exactly what you want from a resume.<span class="qe">&rdquo;</span></blockquote>
    <cite>by Author Name</cite>
  </div>
  <div class="abs divider" style="top:346px"></div>
  <div class="abs story" style="top:365px;left:15px">
    <div class="abs story-photo" role="img" aria-label="Portrait photo of a smiling nurse"></div>
    <blockquote><span class="q">&ldquo;</span>BPP &nbsp;is the perfect solution job seekers are looking for, provided you have content with special language (for objective, goals section etc.) ready beforehand. If you don't, you might want to sit down first and think through exactly what you want from a resume.<span class="qe">&rdquo;</span></blockquote>
    <cite>by Author Name</cite>
  </div>
</section>

<footer class="abs footer">
  <div class="abs foot-nav">Main<span>|</span>About Us<span>|</span>Get Job<span>|</span>Post Now<span>|</span>Update<span>|</span>Contact</div>
  <div class="abs copy">&copy; 2012 Company Name &nbsp;| &nbsp;All right reserved</div>
</footer>

</body>
</html>
```